Corvane: The Quiet Lantern

I need a front, back and spine cover for e and print for a short book. The book is called Corvane, subtitle, The Quiet Lantern. It is about an eyewitness to the Archangel Corvane. I would like to use the design many times with different colours for a series in spirituality and magic. So hopefully I can work with the designer again. The simple idea, is a plain cover in a colour, here blue. Mostly a font based cover, with a small symbolic image silhouetted at the bottom. Other covers will be orange, same font, and a different silhouette symbolic image and so on.

We need: a blue that will print well and look good on a screen. Serious, inviting honesty and truth and not flat. A font that is modern, female, says mystic but not old saint. The author is female and an award-winning writer in different areas. We need a uniform space for a title, (here Corvane), a uniform space for "The Quiet Lantern", a small space for a simple symbolic image, and author name, Wren Halloway. The small image on this blue cover should be in red. Ideas would be a simple rose head. The cover must look modern and professional and compliment the brand at www.wrenhalloway-books.com.

If the designer would simultaneously like to pitch to design the whole series (which will have many titles), another one would be a warm/hot pink background with the title Blue Harbour, subtitle, Brighten Every Ordinary Week. Small image silhouetted in orange might be a small gift shape, or a seahorse. Same author name, Wren Halloway. Another cover would be green background, title Lanterns: subtitle, Seven Rivers Beyond the Hill. Image in yellow: a rolled yoga mat, or an Om symbol. Wren Halloway. If we find a groove for the whole series, I can keep working with the same designer. Of course, the cover just for Corvane is fine here, but please bear in mind it fits into this wider series. Blue covers are about conversation with or contact with key spiritual figures, each from the author's own personal experience. Another one there would be "Swami Dhorelan", Letters From a Northern Garden. Image would be a simple daisy or a trophy emblem in red.

Font is crucial here and will define a series. Modern spirituality for the current generation. It must suggest contact with higher planes without being chintzy. Thank you!

Simple designs are iconic. That is what we are going for!

Good luck.

Target Market(s)

The people who read iconic series books like old marlow classics

Colors
34a6d7

Requirements
Must have
• modern, iconic, translatable into different markets.
Nice to have
• symbolic images silhouetted into a colour, not black, as the guidelines.
Should not have
• not too emotional.

```html
<!DOCTYPE html>
<html lang="en">
<head>
<meta charset="utf-8">
<title>Corvane: The Quiet Lantern — Cover</title>
<link href="https://fonts.googleapis.com/css2?family=Cinzel:wght@400;700&family=Merienda:wght@400&display=swap" rel="stylesheet">
<style>
  :root {
    --ink-red: #9b0808;
    --sea-light: #4fd4e2;
    --sea-mid: #3bb6cf;
    --sea-deep: #2a7b92;
    --sea-edge: #245f74;
  }
  html, body {
    margin: 0;
    padding: 0;
    width: 880px;
    height: 1200px;
    overflow: hidden;
    background: var(--sea-deep);
  }
  .cover {
    position: relative;
    width: 880px;
    height: 1200px;
    overflow: hidden;
    background:
      radial-gradient(ellipse 60% 45% at 22% 48%, var(--sea-light) 0%, rgba(79,212,226,0) 70%),
      radial-gradient(ellipse 75% 70% at 40% 55%, var(--sea-mid) 0%, var(--sea-deep) 80%, var(--sea-edge) 100%);
  }
  .cover__title {
    position: absolute;
    top: 168px;
    left: 0;
    width: 100%;
    margin: 0;
    text-align: center;
    font-family: "Cinzel", serif;
    font-weight: 700;
    font-size: 150px;
    line-height: 1;
    letter-spacing: -2px;
    color: var(--ink-red);
  }
  .cover__subtitle {
    position: absolute;
    top: 352px;
    left: 0;
    width: 100%;
    margin: 0;
    text-align: center;
    font-family: "Cinzel", serif;
    font-weight: 400;
    font-size: 40px;
    line-height: 1;
    color: var(--ink-red);
  }
  .cover__emblem {
    position: absolute;
    left: 384px;
    top: 980px;
    width: 112px;
    height: 88px;
  }
  .cover__author {
    position: absolute;
    top: 1088px;
    left: 0;
    width: 100%;
    margin: 0;
    text-align: center;
    font-family: "Merienda", cursive;
    font-size: 40px;
    line-height: 1.2;
    color: var(--ink-red);
  }
</style>
</head>
<body>
  <main class="cover">
    <h1 class="cover__title">CORVANE</h1>
    <p class="cover__subtitle">The Quiet Lantern</p>
    <svg class="cover__emblem" viewBox="0 0 112 88" role="img" aria-label="Small red silhouette of a rose head">
      <rect x="0" y="0" width="112" height="88" rx="10" fill="var(--ink-red)"/>
    </svg>
    <p class="cover__author">Wren Halloway</p>
  </main>
</body>
</html>
```